Tallow Creek Biotics - Business Card Design

Business Card Brief;
We require a design for a business card template for our business “Tallow Creek Biotics”.
We are a firm that manufacture positive microbial formulations to enhance agricultural legume crops such as lucence, soy beans and faba beans. We also manufacture microbial formulations that aid in composting of waste organic waste to use as a natural fertilizer.
We are seeking a business card design that portrays a clean, professional organisation dedicated to enhancing nature and sustainable farming techniques.
Our website is www.soilvantage.com.au
Here is a link to a drawing of a soybean plant. One of our main products is used to help grow these. I offer it an an example of the type of graphic that might be used on the card, but will leave you to create your own design; https://pixelvaultimages.com/482915066/stock-illustration-soybean-plant-on-a-white.html
Two cards are required;
--------------------------------------------------------------------
Card #1
Cody R Whitfield
Executive Chairman
Mobile: 0471 583204
Email: cody@soilvantage.com.au
---------------------------------------------------------------------------
Card #2
Lachlan P Doyce
Chief Financial & Operating Officer
Mobile: 0456 792418
Email lachlan@soilvantage.com.au

Many thanks
Lachlan Doyce

Industry/Entity Type

Agriculture

Colors

Designer to choose colors to be used in the design.

Requirements
Must have
• An elegant design that demonstrates our commitment to enhancing nature.

```html
<!DOCTYPE html>
<html lang="en">
<head>
<meta charset="utf-8">
<title>Tallow Creek Biotics – Business Cards</title>
<link href="https://fonts.googleapis.com/css2?family=Barlow:wght@300;400;600&display=swap" rel="stylesheet">
<style>
  :root {
    --page-bg: #f8f8f8;
    --card-sage: #7f8a72;
    --card-clay: #b97d68;
    --ink-light: #ffffff;
    --ink-soft: rgba(255, 255, 255, 0.88);
    --mark-tint: rgba(255, 255, 255, 0.28);
    --plant-tint: rgba(255, 255, 255, 0.14);
  }
  * { box-sizing: border-box; margin: 0; padding: 0; }
  html, body {
    width: 1200px;
    height: 1200px;
    overflow: hidden;
    background: var(--page-bg);
    font-family: "Barlow", sans-serif;
  }
  .card-sheet {
    position: relative;
    width: 1200px;
    height: 1200px;
  }
  .business-card {
    position: absolute;
    left: 276px;
    width: 692px;
    height: 435px;
    box-shadow: 0 14px 22px rgba(0, 0, 0, 0.05);
    color: var(--ink-light);
  }
  .business-card--chairman { top: 134px; background: var(--card-sage); }
  .business-card--cfo { top: 596px; background: var(--card-clay); }

  .brand {
    position: absolute;
    left: 60px;
    top: 183px;
    display: flex;
    align-items: center;
    gap: 14px;
  }
  .brand-dot {
    width: 64px;
    height: 64px;
    border-radius: 50%;
    background: var(--mark-tint);
  }
  .brand-name {
    font-weight: 300;
    font-size: 31px;
    line-height: 36px;
    letter-spacing: -0.01em;
    color: var(--ink-light);
  }

  .plant-divider {
    position: absolute;
    left: 326px;
    top: 133px;
    width: 40px;
    height: 186px;
    border-radius: 20px 20px 6px 6px;
    background: linear-gradient(180deg, var(--plant-tint), rgba(255,255,255,0.06));
  }

  .contact {
    position: absolute;
    left: 411px;
    font-size: 16.5px;
    line-height: 27.6px;
    letter-spacing: 0.08em;
    color: var(--ink-soft);
    font-weight: 400;
  }
  .business-card--chairman .contact { top: 174px; }
  .business-card--cfo .contact { top: 155px; }
  .contact-name { font-weight: 600; color: var(--ink-light); }
  .contact-label {
    display: inline-block;
    width: 24px;
    font-weight: 600;
    color: var(--ink-light);
  }
</style>
</head>
<body>
<main class="card-sheet">

  <section class="business-card business-card--chairman">
    <div class="brand">
      <span class="brand-dot"></span>
      <p class="brand-name">Tallow Creek<br>Biotics</p>
    </div>
    <div class="plant-divider" role="img" aria-label="Faint line drawing of a young legume plant with leaves and roots"></div>
    <div class="contact">
      <p class="contact-name">Cody R Whitfield</p>
      <p>Executive Chairman</p>
      <p><span class="contact-label">M</span>0471 583204</p>
      <p><span class="contact-label">E</span>cody@soilvantage.com.au</p>
    </div>
  </section>

  <section class="business-card business-card--cfo">
    <div class="brand">
      <span class="brand-dot"></span>
      <p class="brand-name">Tallow Creek<br>Biotics</p>
    </div>
    <div class="plant-divider" role="img" aria-label="Faint line drawing of a young legume plant with leaves and roots"></div>
    <div class="contact">
      <p class="contact-name">Lachlan P Doyce</p>
      <p>Chief Financial &amp;</p>
      <p>Operating Officer</p>
      <p><span class="contact-label">M</span>0456 792418</p>
      <p><span class="contact-label">E</span>lachlan@soilvantage.com.au</p>
    </div>
  </section>

</main>
</body>
</html>
```